Design a compelling Tarnwell Business Card that will drive people to my site

I want a business card that I can give to people—less to tell them who I am and more to direct them to my website. My website is a portal for Crestlane Aquatics Officials and a place for people who want to become Crestlane Aquatics Officials.
I am uploading my official company logo as well as a business card mockup that I did on my own. Please feel free to completely stray from this design.
I've included a screen recording of the homepage of my website as well.
Target Market(s)
Crestlane Aquatics Officials and people who desire to become one
Contact Information for Business Card
website url
Look and feel
Each slider illustrates characteristics of the customer's brand and the style your logo design should communicate.

```html
<!DOCTYPE html>
<html lang="en">
<head>
<meta charset="utf-8">
<title>Tarnwell Business Card</title>
<link rel="stylesheet" href="https://fonts.googleapis.com/css2?family=Open+Sans:wght@400;700&display=swap">
<style>
  :root {
    --backdrop: #3a3b3d;
    --card-white: #f7f7f8;
    --brand-navy: #2b3f9a;
    --wave-blue: #b9c8e3;
    --text-grey: #4a4a4f;
  }
  * { margin: 0; padding: 0; box-sizing: border-box; }
  html, body {
    width: 1200px;
    height: 900px;
    overflow: hidden;
    background: var(--backdrop);
    font-family: "Open Sans", sans-serif;
  }
  .stage { position: relative; width: 1200px; height: 900px; }
  .card {
    position: absolute;
    width: 560px;
    height: 320px;
    background: var(--card-white);
    box-shadow: 0 10px 24px rgba(0,0,0,0.45);
    overflow: hidden;
  }
  .card--front { left: 60px; top: 100px; }
  .card--back { left: 580px; top: 480px; }
  .card__wave { position: absolute; inset: 0; width: 100%; height: 100%; }
  .wave-fill { fill: var(--wave-blue); }

  .wordmark {
    position: absolute;
    font-weight: 700;
    color: var(--brand-navy);
    letter-spacing: -1px;
    line-height: 1;
  }
  .card--front .wordmark { right: 70px; top: 70px; font-size: 72px; text-align: right; }
  .wordmark__domain { display: block; font-size: 22px; letter-spacing: 0; margin-top: 2px; }
  .card--back .wordmark { right: 50px; top: 48px; font-size: 54px; }

  .contact { position: absolute; left: 58px; top: 150px; }
  .contact__name { font-weight: 700; font-size: 17px; color: var(--brand-navy); }
  .contact__role { font-size: 14px; color: var(--text-grey); margin-bottom: 22px; }
  .contact__line {
    display: flex; align-items: center; gap: 8px;
    font-size: 14px; color: var(--text-grey); margin-bottom: 6px;
  }
  .contact__icon { width: 14px; height: 14px; fill: var(--brand-navy); }
</style>
</head>
<body>
<main class="stage">
  <section class="card card--front" aria-label="Card front">
    <svg class="card__wave" viewBox="0 0 560 320" preserveAspectRatio="none" aria-hidden="true">
      <path class="wave-fill" d="M0,292 C150,292 240,262 300,205 C360,148 450,112 560,100 L560,320 L0,320 Z"/>
    </svg>
    <div class="wordmark">tarnwell<span class="wordmark__domain">.com</span></div>
  </section>

  <section class="card card--back" aria-label="Card back">
    <svg class="card__wave" viewBox="0 0 560 320" preserveAspectRatio="none" aria-hidden="true">
      <path class="wave-fill" d="M0,302 C190,302 260,262 330,205 C400,150 480,122 560,112 L560,320 L0,320 Z"/>
    </svg>
    <div class="wordmark">tarnwell</div>
    <div class="contact">
      <p class="contact__name">Marcus Ellery</p>
      <p class="contact__role">CEO &amp; Founder</p>
      <p class="contact__line">
        <svg class="contact__icon" viewBox="0 0 24 24" aria-hidden="true"><path d="M6.6 10.8a15.1 15.1 0 0 0 6.6 6.6l2.2-2.2a1 1 0 0 1 1-.25 11.4 11.4 0 0 0 3.6.57 1 1 0 0 1 1 1V20a1 1 0 0 1-1 1A17 17 0 0 1 3 4a1 1 0 0 1 1-1h3.5a1 1 0 0 1 1 1c0 1.25.2 2.45.57 3.6a1 1 0 0 1-.25 1z"/></svg>
        (555) 214-7730
      </p>
      <p class="contact__line">
        <svg class="contact__icon" viewBox="0 0 24 24" aria-hidden="true"><path d="M2 5h20v14H2z M3.5 6.5 12 13l8.5-6.5" fill="none" stroke="currentColor"/><path d="M2 5h20v14H2V5zm2 2v.4l8 5.6 8-5.6V7H4z"/></svg>
        marcus@tarnwell.com
      </p>
    </div>
  </section>
</main>
</body>
</html>
```